Carry On Personal Training Sessions

Whether you have a lot to give out or a little...just Carry On. Whether you are strong or you desire to get there... just Carry On. Stay Bold Feel Free. PT's with a passionate coach.

I had imagined black and white or indigo/white. Communicate love, people and fitness.

Target Market(s)

Women, men, disabilities. People whom wish to move more, or who do not desire to go to a gym. One on one fitness or small group training.

Industry/Entity Type

Training

Contact Information for Business Card

Kim Harlow
0431 592 647
kimjoanne@fernmail.com

Font styles to use
Decorative

Colors
0d0d0d
1b1b1b

Requirements
Must have
• Carry On
• Personal Fitness Sessions
• Stay Bold Feel Free
• ( my details above )
Nice to have
• If any part of the project description ....Whether....etc
• can be fit onto card. That would be great. I had ideas of Heart, people exercising, I love boxing training, so this idea was in my head, not sure how to bring all together. Would also like to work with disabilities.
Should not have
• Cannot think of any not haves at this stage.
• Colours at the bottom of page, either green is ok, with charcoal or navy. Not both these colours together.

```html
<!DOCTYPE html>
<html lang="en">
<head>
<meta charset="utf-8">
<title>Carry On Personal Training Sessions – Business Card</title>
<link rel="stylesheet" href="https://fonts.googleapis.com/css2?family=Michroma&family=Allura&family=Roboto+Condensed:wght@500;700&display=swap">
<style>
  :root {
    --backdrop: #262626;
    --card-deep: #0d0d0d;
    --card-soft: #1b1b1b;
    --ink: #ffffff;
    --badge: #8a98a6;
  }
  * { margin: 0; padding: 0; box-sizing: border-box; }
  html, body {
    width: 1200px;
    height: 900px;
    overflow: hidden;
    background: var(--backdrop);
  }
  .stage { position: relative; width: 1200px; height: 900px; }
  .card {
    position: absolute;
    left: 285px;
    width: 642px;
    height: 377px;
    background: linear-gradient(160deg, var(--card-soft) 0%, var(--card-deep) 70%);
    color: var(--ink);
    box-shadow: 0 6px 14px rgba(0,0,0,0.55);
  }
  .card--front { top: 60px; }
  .card--back { top: 470px; }

  .mark-circle {
    position: absolute;
    border-radius: 50%;
    background: var(--ink);
  }
  .card--front .mark-circle { left: 248px; top: 48px; width: 146px; height: 146px; }
  .card--back .mark-circle { left: 90px; top: 62px; width: 128px; height: 128px; }

  .brand-name {
    position: absolute;
    left: 0; width: 100%;
    top: 230px;
    text-align: center;
    font-family: "Michroma", sans-serif;
    font-size: 38px;
    letter-spacing: 1px;
  }
  .brand-sub {
    position: absolute;
    left: 0; width: 100%;
    top: 282px;
    text-align: center;
    font-family: "Michroma", sans-serif;
    font-size: 13px;
  }
  .brand-tagline {
    position: absolute;
    left: 0; width: 100%;
    top: 298px;
    text-align: center;
    font-family: "Allura", cursive;
    font-size: 34px;
  }

  .contact {
    position: absolute;
    left: 10px; width: 294px;
    top: 215px;
    text-align: center;
    font-family: "Michroma", sans-serif;
  }
  .contact__name { font-size: 20px; letter-spacing: 1px; margin-bottom: 8px; }
  .contact__line { font-size: 13px; line-height: 20px; }

  .divider {
    position: absolute;
    left: 312px; top: 90px;
    width: 4px; height: 198px;
    background: var(--ink);
  }
  .manifesto {
    position: absolute;
    left: 335px; top: 86px;
    font-family: "Roboto Condensed", sans-serif;
    font-weight: 700;
    text-transform: uppercase;
    line-height: 1.15;
  }
  .manifesto p { font-size: 17px; font-weight: 500; }
  .manifesto .manifesto__call { font-size: 33px; font-weight: 700; line-height: 1.05; }
  .manifesto .manifesto__motto { font-size: 24px; font-weight: 700; }

  .partner-badge {
    position: absolute;
    left: 440px; top: 318px;
    width: 144px; height: 30px;
    border-radius: 3px;
    background: var(--badge);
    opacity: 0.55;
  }
</style>
</head>
<body>
<main class="stage">
  <section class="card card--front" aria-label="Card front">
    <div class="mark-circle"></div>
    <h1 class="brand-name">CARRY ON</h1>
    <p class="brand-sub">PERSONAL FITNESS SESSIONS</p>
    <p class="brand-tagline">Stay Bold Feel Free</p>
  </section>

  <section class="card card--back" aria-label="Card back">
    <div class="mark-circle"></div>
    <div class="contact">
      <p class="contact__name">KIM HARLOW</p>
      <p class="contact__line">Phone: 0431 592 647</p>
      <p class="contact__line">kimjoanne@fernmail.com</p>
      <p class="contact__line">ABN: 48207719356</p>
    </div>
    <div class="divider"></div>
    <div class="manifesto">
      <p>Whether you have a lot to<br>give out or a little...</p>
      <p class="manifesto__call">Just Carry On.</p>
      <p>Whether you are strong or<br>you desire to get there</p>
      <p class="manifesto__call">Just Carry On.</p>
      <p class="manifesto__motto">Stay Bold Feel Free.</p>
      <p>PT's with a passionate coach.</p>
    </div>
    <div class="partner-badge" role="img" aria-label="Industry association membership badge"></div>
  </section>
</main>
</body>
</html>
```